Simple and elegant Wallsaver Packaging needed for our new product

We are looking for a packaging for our new wallsaver product, which primary purpose is to protect damages to the wall. It prevents drilling holes into the wall.

Packaging file can be found - https://files.qeltorashare.com/open?id=7Kxm2RtQvbLwNpZcYhDsFjUeAgVo

The company name is Brantova and i have attached pictures of the product and the company logo that we would like on the packaging.

Examples of packaging we like in terms of packaging are pordane packaging and fenwick & mallory packaging.

Copies of instructions to set up the product are on the 5th picture on this link - https://www.tradomix.co.uk/d/kpw/Velsora-Pressure-Protect-Surface-Gates-Curtain-Tension-Mounted/Z93H4TQ2LM.
Updates

All,I have updated the brief and add more info about the packaging so please have another look.I look forward to receiving your designs and giving feedback.Thanks Added Thursday, January 12, 2017

Hi All, We still awaiting for more entries before making our final decision. Happy to assist if anyone has further queries. Thanks

One more day left so please submit your designs. I will be giving feedback shortly on the designs received so far. A few designers have asked for me to extend the competition so they have time to submit, so i may do this. Regards Tessa

Reason: Hi, I am extending the deadline so designers can incorporate the feedback i am going to give. So i can get the best possible design possible. Thanks

Target Market(s)

Homeowners

Industry/Entity Type

Home Improvement

Requirements
Must have
• Logo, Instructions to use
Nice to have
• Pictures of product

```html
<!DOCTYPE html>
<html lang="en">
<head>
<meta charset="utf-8">
<title>Brantova Wall Saver Packaging</title>
<link rel="stylesheet" href="https://fonts.googleapis.com/css2?family=Montserrat:wght@400;500;600&family=Archivo+Black&family=Roboto+Condensed:ital,wght@0,400;1,400&display=swap">
<style>
  :root{
    --bg:#b4b9bb;
    --charcoal:#3c3c3d;
    --ink:#3a3a3a;
    --paper:#ffffff;
    --tag:#efdcb6;
    --disc:#e6e8ea;
    --photo-a:#d9d2c6;
    --photo-b:#8a8f92;
  }
  .variant-amber{--accent:#e8b14b;--ring:#e8b14b;--ring-mid:#353535;}
  .variant-mint{--accent:#b7ddd2;--ring:#9fd0c2;--ring-mid:#9fd0c2;}
  *{box-sizing:border-box;margin:0;padding:0}
  html,body{width:1200px;height:722px;overflow:hidden;background:var(--bg)}
  .canvas{position:relative;width:1200px;height:722px;display:flex;justify-content:center;align-items:center;gap:60px}
  .carton{display:flex;box-shadow:0 10px 24px rgba(0,0,0,.18)}
  .front,.side{position:relative;height:290px;background:var(--paper);overflow:hidden}
  .front{width:340px}
  .side{width:170px;border-left:1px solid #d6d6d6}
  .band-top{position:absolute;left:0;top:0;width:100%;height:56px;background:var(--charcoal)}
  .band-accent{position:absolute;left:0;top:56px;width:100%;height:96px;background:var(--accent)}
  .brand{position:absolute;top:12px;color:#fff;font-family:"Montserrat",sans-serif;font-weight:500;letter-spacing:2px;text-align:center}
  .front .brand{left:60px;right:0;font-size:22px}
  .side .brand{left:0;right:0;top:18px;font-size:14px}
  .tagline{position:absolute;color:#fff;font-family:"Montserrat",sans-serif;font-size:6.5px;letter-spacing:1.6px;text-align:center}
  .front .tagline{left:60px;right:0;top:40px}
  .side .tagline{left:0;right:0;top:37px;font-size:4.5px;letter-spacing:1px}
  .photo-column{position:absolute;left:8px;top:62px;display:flex;flex-direction:column;gap:8px}
  .photo-dot{width:64px;height:64px;border-radius:50%;border:3px solid var(--ring);background:linear-gradient(160deg,var(--photo-a),var(--photo-b))}
  .photo-dot.mid{border-color:var(--ring-mid);background:linear-gradient(160deg,#f1f1f1,#bfc3c5)}
  .product-shot{position:absolute;left:126px;top:74px;width:200px;height:190px;border-radius:46% 46% 48% 42%;background:radial-gradient(circle at 45% 40%,#fbfbfb,var(--disc) 70%,#cfd3d6)}
  .title{position:absolute;left:78px;top:92px;font-family:"Archivo Black",sans-serif;font-style:italic;font-size:38px;color:var(--ink);letter-spacing:-.5px;-webkit-text-stroke:1px #fff;transform:skewX(-8deg)}
  .flag{position:absolute;left:92px;z-index:1;padding:3px 14px;font-family:"Montserrat",sans-serif;color:var(--ink)}
  .flag::before{content:"";position:absolute;inset:0;background:var(--tag);transform:skewX(-18deg);z-index:-1;opacity:.9}
  .flag.pack{top:184px;font-size:15px;font-style:italic;font-weight:500;width:140px;text-align:center}
  .flag.feature{font-size:7.5px;line-height:1.35}
  .flag.f1{top:216px;white-space:nowrap}
  .flag.f2{top:240px;width:232px}
  .bullets{position:absolute;left:10px;right:10px;top:66px;list-style:none;font-family:"Roboto Condensed",sans-serif;font-size:5.5px;color:#3a3a3a;line-height:1.3}
  .bullets li{position:relative;padding-left:8px;margin-bottom:9px}
  .bullets li::before{content:"";position:absolute;left:0;top:1px;width:3px;height:10px;background:var(--charcoal)}
  .copy{position:absolute;left:10px;right:12px;top:164px;font-family:"Roboto Condensed",sans-serif;font-style:italic;font-size:5.5px;color:#333;line-height:1.35}
  .copy p{margin-bottom:8px}
  .copy .link{overflow-wrap:anywhere}
</style>
</head>
<body>
<main class="canvas">
  <section class="carton variant-amber">
    <div class="front">
      <div class="band-top"></div>
      <div class="band-accent"></div>
      <div class="brand">BRANTOVA</div>
      <div class="tagline">HOMEWARE ACCESSORIES</div>
      <div class="photo-column">
        <div class="photo-dot" role="img" aria-label="Safety gate fitted in a doorway"></div>
        <div class="photo-dot mid" role="img" aria-label="Close-up of wall saver pad holding a gate spindle"></div>
        <div class="photo-dot" role="img" aria-label="Gate installed at the top of a staircase"></div>
      </div>
      <div class="product-shot" role="img" aria-label="Two white wall saver discs, front and back"></div>
      <div class="title">Wall Saver</div>
      <div class="flag pack">SAVER 2 PACK</div>
      <div class="flag feature f1">Easy Fast Installation, No Tools Required</div>
      <div class="flag feature f2">Oversized Pad Protects Walls Better, Large Surface Area Makes For More Stable Installation</div>
    </div>
    <div class="side">
      <div class="band-top"></div>
      <div class="band-accent"></div>
      <div class="brand">BRANTOVA</div>
      <div class="tagline">HOMEWARE ACCESSORIES</div>
      <ul class="bullets">
        <li>Secure hold on stair rails and door frames, no drilling.</li>
        <li>Compatible with most pressure mounted gates and curtain rods.</li>
        <li>Non-slip base keeps walls free of marks.</li>
        <li>Includes 2 pads, white finish.</li>
      </ul>
      <div class="copy">
        <p>The company name is Brantova and i have attached pictures of the product and the company logo that we would like on the packaging.</p>
        <p>Examples of packaging we like in terms of packaging are pordane packaging and fenwick &amp; mallory packaging.</p>
        <p>Copies of instructions to set up the product are on the 5th picture on this link - <span class="link">https://www.tradomix.co.uk/d/kpw/Velsora-Pressure-Protect-Surface-Gates-Curtain-Tension-Mounted/Z93H4TQ2LM</span></p>
      </div>
    </div>
  </section>

  <section class="carton variant-mint">
    <div class="front">
      <div class="band-top"></div>
      <div class="band-accent"></div>
      <div class="brand">BRANTOVA</div>
      <div class="tagline">HOMEWARE ACCESSORIES</div>
      <div class="photo-column">
        <div class="photo-dot" role="img" aria-label="Safety gate fitted in a doorway"></div>
        <div class="photo-dot mid" role="img" aria-label="Close-up of wall saver pad holding a gate spindle"></div>
        <div class="photo-dot" role="img" aria-label="Gate installed at the top of a staircase"></div>
      </div>
      <div class="product-shot" role="img" aria-label="Two white wall saver discs, front and back"></div>
      <div class="title">Wall Saver</div>
      <div class="flag pack">SAVER 2 PACK</div>
      <div class="flag feature f1">Easy Fast Installation, No Tools Required</div>
      <div class="flag feature f2">Oversized Pad Protects Walls Better, Large Surface Area Makes For More Stable Installation</div>
    </div>
    <div class="side">
      <div class="band-top"></div>
      <div class="band-accent"></div>
      <div class="brand">BRANTOVA</div>
      <div class="tagline">HOMEWARE ACCESSORIES</div>
      <ul class="bullets">
        <li>Secure hold on stair rails and door frames, no drilling.</li>
        <li>Compatible with most pressure mounted gates and curtain rods.</li>
        <li>Non-slip base keeps walls free of marks.</li>
        <li>Includes 2 pads, white finish.</li>
      </ul>
      <div class="copy">
        <p>The company name is Brantova and i have attached pictures of the product and the company logo that we would like on the packaging.</p>
        <p>Examples of packaging we like in terms of packaging are pordane packaging and fenwick &amp; mallory packaging.</p>
        <p>Copies of instructions to set up the product are on the 5th picture on this link - <span class="link">https://www.tradomix.co.uk/d/kpw/Velsora-Pressure-Protect-Surface-Gates-Curtain-Tension-Mounted/Z93H4TQ2LM</span></p>
      </div>
    </div>
  </section>
</main>
</body>
</html>
```